Wendelmarsh general contractors post card for mailing

Ideas: bathrooms, basements, kitchens, drywall, painting, landscaping, plumbing, electric, appliance, flooring, trim, sheds, decks, fences, home building, commercial construction, property management, lawn care/maintenance Just to list a few!!!

If we can't do it... it can't be done right.

turning dreams and aspirations into affordable reality.

Did your last contractor fail to meet your expectations? Let us provide affordable corrections.

Your single point of success for all your repair, replace, renovation, and building needs.

Trust us with all your projects large and small.

Target Market(s)

Home owners commercial property owners

Industry/Entity Type

Construction Company

Requirements
Must have
• phone number in red
Nice to have
• I would like to see greyscale background of commercial and suburban housing as a faded canvas backdrop.

```html
<!DOCTYPE html>
<html lang="en">
<head>
<meta charset="utf-8">
<title>Wendelmarsh General Contractors – Postcard</title>
<link href="https://fonts.googleapis.com/css2?family=Oswald:wght@500;600;700&family=Libre+Baskerville:wght@400;700&family=Open+Sans:wght@400;600;700&display=swap" rel="stylesheet">
<style>
  :root {
    --navy: #1f2a6b;
    --navy-deep: #161f55;
    --red: #e0222b;
    --white: #ffffff;
    --ink: #1c2340;
    --page: #e9e9ec;
    --sky-top: #8fb0d8;
    --sky-low: #3e5f94;
    --house-light: #e4e4e4;
    --house-dark: #a9a9a9;
  }
  * { box-sizing: border-box; margin: 0; padding: 0; }
  html, body { width: 900px; height: 1200px; overflow: hidden; background: var(--page); }
  body { position: relative; font-family: "Open Sans", Arial, sans-serif; }

  .card {
    position: absolute; left: 40px; width: 820px; height: 555px;
    background: var(--white); overflow: hidden;
    box-shadow: 0 4px 14px rgba(0,0,0,.18);
  }
  .card--front { top: 30px; }
  .card--back { top: 615px; }
  .card svg.shapes { position: absolute; inset: 0; }

  .brand { position: absolute; display: flex; align-items: center; gap: 9px; }
  .brand__mark { width: 18px; height: 18px; background: var(--navy); }
  .brand__name {
    font-family: "Libre Baskerville", Georgia, serif; font-weight: 700;
    color: var(--navy); font-size: 21px; letter-spacing: .5px; white-space: nowrap;
  }
  .card--front .brand { left: 40px; top: 64px; }
  .card--back .brand { left: 40px; top: 42px; }

  /* front */
  .front__headline { position: absolute; left: 40px; top: 318px; font-family: "Oswald", Arial, sans-serif; font-weight: 600; text-transform: uppercase; line-height: 1.05; }
  .front__headline .line-a { color: var(--white); font-size: 44px; display: block; }
  .front__headline .line-b { color: var(--red); font-size: 48px; display: block; }
  .front__tagline { position: absolute; left: 40px; top: 434px; font-family: "Libre Baskerville", Georgia, serif; font-weight: 700; color: var(--white); font-size: 25px; }
  .front__callbar {
    position: absolute; left: 28px; right: 28px; top: 486px; height: 46px;
    background: var(--red); border: 2px solid var(--white); border-radius: 8px;
    display: flex; align-items: center; justify-content: space-between; padding: 0 18px;
    font-family: "Oswald", Arial, sans-serif; font-weight: 600; color: var(--white); font-size: 26px;
  }
  .front__callbar .web { font-family: "Open Sans", Arial, sans-serif; font-weight: 700; font-size: 22px; }

  /* back */
  .back__question { position: absolute; left: 40px; top: 100px; width: 400px; font-family: "Oswald", Arial, sans-serif; font-weight: 600; color: var(--navy); font-size: 24px; line-height: 1.15; text-transform: uppercase; }
  .back__offer { position: absolute; left: 40px; top: 168px; width: 430px; height: 38px; background: var(--red); color: var(--white); font-family: "Oswald", Arial, sans-serif; font-weight: 600; font-size: 22px; display: flex; align-items: center; padding-left: 14px; text-transform: uppercase; }
  .services { position: absolute; left: 40px; top: 212px; width: 430px; height: 136px; background: var(--navy); display: grid; grid-template-columns: 120px 120px 170px; padding: 10px 14px; list-style: none; color: var(--white); font-size: 12.5px; line-height: 1.36; column-gap: 4px; }
  .services ul { list-style: none; }
  .services li::before { content: ""; display: inline-block; width: 6px; height: 6px; background: var(--red); margin-right: 6px; vertical-align: 2px; }
  .back__promise { position: absolute; left: 40px; top: 362px; width: 420px; color: var(--navy); font-size: 15px; line-height: 1.4; font-weight: 600; }
  .back__trust { position: absolute; left: 40px; top: 420px; border: 2px solid var(--red); color: var(--navy); font-family: "Libre Baskerville", Georgia, serif; font-size: 15px; padding: 4px 12px; }
  .back__call { position: absolute; left: 40px; top: 460px; font-family: "Oswald", Arial, sans-serif; font-weight: 600; font-size: 30px; color: var(--navy); }
  .back__call .phone { color: var(--red); }
  .back__web { position: absolute; left: 40px; top: 506px; font-family: "Oswald", Arial, sans-serif; font-weight: 500; font-size: 24px; color: var(--navy); letter-spacing: 2px; }
  .stamp { position: absolute; right: 40px; top: 36px; width: 80px; height: 96px; border: 2px solid #b8b8b8; background: rgba(255,255,255,.6); }
</style>
</head>
<body>

<section class="card card--front" aria-label="Postcard front">
  <svg class="shapes" width="820" height="555" viewBox="0 0 820 555">
    <defs>
      <linearGradient id="skyline" x1="0" y1="0" x2="0" y2="1">
        <stop offset="0" stop-color="var(--sky-top)"/>
        <stop offset="1" stop-color="var(--sky-low)"/>
      </linearGradient>
    </defs>
    <g role="img" aria-label="Photo of glass skyscrapers against a blue sky">
      <polygon points="310,0 820,0 820,252 405,278" fill="url(#skyline)"/>
    </g>
    <polygon points="0,302 820,252 820,555 0,555" fill="var(--navy)"/>
    <line x1="310" y1="0" x2="405" y2="278" stroke="var(--navy)" stroke-width="8"/>
    <line x1="0" y1="302" x2="820" y2="252" stroke="var(--white)" stroke-width="4"/>
    <line x1="0" y1="312" x2="820" y2="262" stroke="var(--red)" stroke-width="3"/>
  </svg>
  <div class="brand"><span class="brand__mark"></span><span class="brand__name">WENDELMARSH</span></div>
  <h1 class="front__headline"><span class="line-a">If we can't do it</span><span class="line-b">It can't be done right</span></h1>
  <p class="front__tagline">Turning dreams and aspirations into affordable reality</p>
  <div class="front__callbar"><span>CALL US TODAY: 1234567890</span><span class="web">www.yourwebsite.com</span></div>
</section>

<section class="card card--back" aria-label="Postcard back">
  <svg class="shapes" width="820" height="555" viewBox="0 0 820 555">
    <defs>
      <linearGradient id="houses" x1="0" y1="0" x2="1" y2="1">
        <stop offset="0" stop-color="var(--house-light)"/>
        <stop offset="1" stop-color="var(--house-dark)"/>
      </linearGradient>
    </defs>
    <g role="img" aria-label="Faded greyscale photo of suburban houses">
      <polygon points="540,0 820,0 820,555 480,555" fill="url(#houses)" opacity=".75"/>
    </g>
    <polygon points="500,0 540,0 480,555 440,555" fill="var(--navy)"/>
    <polygon points="545,0 555,0 495,555 485,555" fill="var(--red)"/>
  </svg>
  <div class="brand"><span class="brand__mark"></span><span class="brand__name">WENDELMARSH</span></div>
  <div class="stamp" aria-label="Stamp area"></div>
  <h2 class="back__question">Did your last contractor fail to meet your expectations?</h2>
  <div class="back__offer">Let us provide affordable corrections</div>
  <div class="services">
    <ul><li>Bathrooms</li><li>Basements</li><li>Kitchen</li><li>Drywall</li><li>Painting</li><li>Trim</li></ul>
    <ul><li>Landscaping</li><li>Plumbing</li><li>Electric</li><li>Appliance</li><li>Flooring</li><li>Sheds</li></ul>
    <ul><li>Decks</li><li>Fences</li><li>Home building</li><li>Commercial construction</li><li>Property management</li><li>Lawn care/maintenance</li></ul>
  </div>
  <p class="back__promise">Your single point of success for all your repair, replace, renovation, and building needs.</p>
  <p class="back__trust">Trust us with all your projects large and small.</p>
  <p class="back__call">CALL US TODAY: <span class="phone">1234567890</span></p>
  <p class="back__web">www.yourwebsite.com</p>
</section>

</body>
</html>
```